VORNel - Visual Oriented Networked Engagement - business cards

3x3 inch business cards
full color
use attached logo with old business card info

VORNEL will design, integrate and manufacture equipment for you to create an engaging, impactful experience for you and your consumer.

MISSION
VORNEL creates content-rich, emotionally compelling, and experiential spaces for a wide range of environments. Helping people find their way, communicate important information, and create unique moment of impact in virtually any environment that communicate with users.

What
You name it we will develop it, from digital wayfinding signage, multimedia installations, user interfaces, in any environment. We strive to enrich the lives of people wherever they work, play, learn, shop, travel, or gather.

HOW
We plan, design, and build a diverse range of visual communication and information systems, to improve the human experience. Dedicated to a collaborative design process that puts user needs first. We work with your ideas to shape a unique user experience that orients, informs, educates and captivates.
Benefits
Improved customer experience
Improved Branding/recall
Sales Lift
Cost savings/efficiency
Ad revenue/ROI
Differentiator from competition
Reduce perceived wait times
Internal communication
Generate inquiries
Safety/security
Better compliance/display control
Responsiveness
Public information
WHERE
Shopping Malls, entertainment and hospitality destinations and other environments are using the tools and story-telling approaches to create more engaging, emotionally compelling and impactful interactions with their customers, guests and users.
Markets
Architectural
Corporate
Education
Entertainment
Exhibition
Government
Healthcare
Hospitality
Residential
Retail
Sports
Tourism
Transportation
Urban
Visitor Centers
Workplace

Target Market(s)

corporate B2B, see attached details

Industry/Entity Type

Digital Signage

Contact Information for Business Card

see personal details from Loftwell business cards apply to new cards

but use

www.vornel-example.com
marla@vornel-example.com

Font styles to use
Other font styles liked:
• century gothic

Colors
0355a3
3277b5
85acd3
34a6d7
0692cd

Requirements
Must have
• existing logo
• want depth and impact from the cards.
• giant dice image on one side of card
• details on the front side of card
• scalable image so you read the words under the logo
• 3inch x 3inch size only
Nice to have
• watermark with big dice image on front or possibly on the back with the cull logo on top of watermark cube.
• same blue color font on logo as on the card
• could use word cloud on the back of card (these are our company values)
Should not have
• should not be blank 2nd side
• should not just/ only redo my attachments - they are only a concept not what I want that's why I am using your services to provide more creativity and better ideas.

```html
<!DOCTYPE html>
<html lang="en">
<head>
<meta charset="utf-8">
<title>VORNEL business cards</title>
<link rel="stylesheet" href="https://fonts.googleapis.com/css2?family=Source+Sans+3:wght@400;600&display=swap">
<style>
  :root {
    --canvas-bg: #e9e7e5;
    --card-white: #ffffff;
    --card-dark: #1f1e1e;
    --ink: #222222;
    --ink-light: #f2f2f2;
  }
  * { margin: 0; padding: 0; box-sizing: border-box; }
  html, body {
    width: 1200px;
    height: 970px;
    overflow: hidden;
    background: var(--canvas-bg);
    font-family: "Source Sans 3", sans-serif;
  }
  .canvas { position: relative; width: 1200px; height: 970px; }
  .card {
    position: absolute;
    width: 408px;
    height: 410px;
    box-shadow: 0 6px 18px rgba(0,0,0,0.12);
  }
  .card--front { left: 204px; top: 166px; background: var(--card-white); color: var(--ink); text-align: center; }
  .card--back { left: 661px; top: 328px; background: var(--card-dark); }

  .person-name { position: absolute; top: 104px; width: 100%; font-size: 20px; font-weight: 600; letter-spacing: 0.2px; }
  .person-title { position: absolute; top: 130px; width: 100%; font-size: 14px; font-weight: 400; }
  .divider { position: absolute; left: 134px; width: 140px; height: 1px; background: var(--ink); }
  .divider--top { top: 174px; }
  .divider--bottom { top: 263px; }
  .contact { position: absolute; top: 186px; width: 100%; font-size: 13.5px; line-height: 21px; }
  .company-name { position: absolute; top: 276px; width: 100%; font-size: 14px; font-weight: 600; }
  .company-address { position: absolute; top: 298px; width: 100%; font-size: 13.5px; }

  .brand-name {
    position: absolute;
    left: 0; top: 180px;
    width: 100%;
    text-align: center;
    font-size: 40px;
    font-weight: 600;
    letter-spacing: 6px;
    color: var(--ink-light);
  }
</style>
</head>
<body>
<main class="canvas">
  <section class="card card--front">
    <h1 class="person-name">MARLA QUINTERO</h1>
    <p class="person-title">Director, Digital Strategies</p>
    <div class="divider divider--top"></div>
    <p class="contact">555.014.2297<br>marla@vornel-example.com<br>www.vornel-example.com</p>
    <div class="divider divider--bottom"></div>
    <p class="company-name">Visual Oriented Networked Engagement</p>
    <p class="company-address">4418-12 street riverton ab t0x2k4 canada</p>
  </section>

  <section class="card card--back">
    <p class="brand-name">VORNEL</p>
  </section>
</main>
</body>
</html>
```